MODERN DESIGN BUSINESS CARDS FOR A CREDIT REPAIR COMPANY

Our goal is to have a modern yet professional business card for our credit repair company. Something that'll catch the eye of our clients. PLEASE BE CREATIVE. WE WOULD LIKE TO SEE HOW THIS WOULD LOOK WITH A WHITE AND BLACK BACK GROUND.

Contact Information for Business Card

THIS WILL BE A DOUBLE SIDED BUSINESS CARD, THE COLORS WE WOULD LIKE TO HAVE IS BLACK, BLUES AND WHITE

Colors
3277b5
33a6d7
ffffff

Requirements
Must have
• MUST HAVE OUR LOGO, BUSINESS PHONE # (956 )482-7153, FACEBOOK LINK FACEBOOK.COM/VORMANTEKCREDITSOLUTIONS, CALL US FOR YOUR FREE CONSULTATION
Nice to have
• ITEMS WE DELETE: LATE PAYMENTS, CHARGE-OFFS, REPOSESSIONS, HOSPITAL BILLS, STUDENT LOANS, FORECLOSURES, CHILD SUPPORT AND BANKRUPTCIES.

```html
<!DOCTYPE html>
<html lang="en">
<head>
<meta charset="utf-8">
<title>Vormantek Credit Solutions – Business Cards</title>
<link href="https://fonts.googleapis.com/css2?family=Montserrat:wght@400;500;700&display=swap" rel="stylesheet">
<style>
  :root {
    --backdrop: #dcdadb;
    --card-white: #ffffff;
    --card-dark: #262626;
    --navy: #123f7c;
    --brand-blue: #1d4e8f;
    --ink: #2b2b2b;
    --muted-ink: #444444;
    --silver: #8c8c8c;
    --badge-blue: #2a5ea8;
    --badge-rim: #16386d;
  }
  * { margin: 0; padding: 0; box-sizing: border-box; }
  html, body {
    width: 1200px; height: 884px; overflow: hidden;
    background: var(--backdrop);
    font-family: "Montserrat", Arial, sans-serif;
  }
  .stage {
    position: relative; width: 1200px; height: 884px;
    display: flex; flex-direction: column; align-items: center; justify-content: center; gap: 36px;
  }
  .card {
    position: relative; width: 680px; height: 388px; overflow: hidden;
    box-shadow: 0 6px 18px rgba(0,0,0,0.18);
  }

  /* Front */
  .card--front { background: var(--card-white); }
  .brand {
    position: absolute; left: 44px; top: 120px; width: 250px;
    display: flex; align-items: center; gap: 12px;
  }
  .brand__mark {
    width: 48px; height: 48px; border-radius: 50%; flex: none;
    background: var(--brand-blue);
  }
  .brand__name {
    color: var(--brand-blue); font-weight: 700; font-size: 25px; line-height: 1.05; letter-spacing: 0.5px;
  }
  .brand__name small { display: block; font-size: 12.5px; letter-spacing: 3px; font-weight: 700; }
  .front__divider {
    position: absolute; left: 318px; top: 70px; width: 1.5px; height: 178px; background: var(--navy);
  }
  .contact { position: absolute; left: 338px; top: 66px; }
  .contact__name { color: var(--navy); font-weight: 700; font-size: 24px; letter-spacing: 0.5px; }
  .contact__title { color: var(--muted-ink); font-size: 13px; margin: 2px 0 14px; }
  .contact__list { list-style: none; }
  .contact__item {
    display: flex; align-items: center; gap: 8px;
    color: var(--ink); font-size: 14.5px; line-height: 27px; letter-spacing: 0.2px;
  }
  .contact__item svg { width: 16px; height: 16px; flex: none; }
  .cta-band {
    position: absolute; left: 0; top: 286px; width: 680px; height: 48px; background: var(--navy);
    color: #fff; font-weight: 500; font-size: 17px; letter-spacing: 1px;
    display: flex; align-items: center; padding-left: 120px;
  }
  .seal {
    position: absolute; left: 578px; top: 262px; width: 76px; height: 76px; border-radius: 50%;
    background: var(--badge-blue); border: 5px solid var(--badge-rim);
  }

  /* Back */
  .card--back { background: var(--card-dark); }
  .brand--back { left: 0; right: 0; top: 96px; width: auto; justify-content: center; gap: 22px; }
  .brand--back .brand__mark { width: 110px; height: 110px; background: var(--silver); }
  .brand--back .brand__name { color: var(--silver); font-size: 62px; letter-spacing: 1px; }
  .brand--back .brand__name small { font-size: 24px; letter-spacing: 9px; }
  .deletions {
    position: absolute; left: 40px; right: 40px; top: 292px;
    color: #f2f2f2; font-size: 15px; line-height: 24px; text-align: center;
  }
</style>
</head>
<body>
<main class="stage">

  <section class="card card--front" aria-label="Business card front">
    <div class="brand">
      <span class="brand__mark"></span>
      <span class="brand__name">VORMANTEK<small>CREDIT SOLUTIONS</small></span>
    </div>
    <div class="front__divider"></div>
    <div class="contact">
      <h1 class="contact__name">DALE HARMON</h1>
      <p class="contact__title">Managing Partner</p>
      <ul class="contact__list">
        <li class="contact__item">
          <svg viewBox="0 0 16 16"><path fill="#123f7c" d="M3 1.5l3 .5 1 3.2-1.8 1.3a8 8 0 0 0 4.3 4.3l1.3-1.8 3.2 1 .5 3c-.2.9-1 1.5-2 1.5A12 12 0 0 1 1.5 3.5c0-1 .6-1.8 1.5-2z"/></svg>
          (956 )482-7153
        </li>
        <li class="contact__item">
          <svg viewBox="0 0 16 16"><rect x="1" y="3" width="14" height="10" rx="1" fill="#123f7c"/><path d="M1.5 3.5L8 9l6.5-5.5" stroke="#fff" stroke-width="1.3" fill="none"/></svg>
          info@vormantekcreditsolutiones.com
        </li>
        <li class="contact__item">
          <svg viewBox="0 0 16 16"><circle cx="8" cy="8" r="6.5" fill="none" stroke="#123f7c" stroke-width="1.6"/><ellipse cx="8" cy="8" rx="2.6" ry="6.5" fill="none" stroke="#123f7c" stroke-width="1.2"/><path d="M1.5 8h13" stroke="#123f7c" stroke-width="1.2"/></svg>
          www.vormantekcreditsolutiones.com
        </li>
        <li class="contact__item">
          <svg viewBox="0 0 16 16"><rect x="1.5" y="1.5" width="13" height="13" rx="2" fill="#123f7c"/></svg>
          facebook/vormantekcreditsolutiones
        </li>
      </ul>
    </div>
    <div class="cta-band">CALL US FOR YOUR FREE CONSULTATION</div>
    <div class="seal" role="img" aria-label="Certification seal"></div>
  </section>

  <section class="card card--back" aria-label="Business card back">
    <div class="brand brand--back">
      <span class="brand__mark"></span>
      <span class="brand__name">VORMANTEK<small>CREDIT SOLUTIONS</small></span>
    </div>
    <p class="deletions">Items we delete: Late payments, charge-offs, repossessions, hospital bills,<br>student loans, foreclosures, child support and bankruptcies.</p>
  </section>

</main>
</body>
</html>
```